CBD Boutique Business Card Needed

We are in need of a business card to reflect the direction of our latest products. We are a fully organic company in which our store and products are very heavy in wood and "natural" components. We decided to bring color into one of our brands and immediately knew this is where we needed to go.

We are NOT a cash grab CBD company. We could have done this wrong, slapped a label on a shit product and left it like that. I am passionate about sharing my experience with other veterans and opening a store and making it a comfortable place for others to come and see if they can have the same experience.

Target Market(s)

We are a dual market company. We do have a beauty line that will cover the costs of the majority of our business. But we also heavily cater to veterans and first responders. I am a veteran and this is how I found out about CBD. So the marketing needs to bring in our higher end beauty clientele but also be able to not put off our customers that readily need this.

Contact Information for Business Card

What we are looking for is a light, professional, boutique design that is is neither quite feminine or masculine. Attached is a picture of a store in Portland that we asked our store designer to get her inspiration from. But all natural wood and black outlines are what is mostly in there.

Attached are the following files:

Logo: An AI file with how we have our logo. I do not understand AI and have no idea why the letters are individual. The font is Adam. OLU is the logo and Tonics of Vigor is our tagline.

KM Vantage (front and back) cards I did originally found at a trade show that I absolutely loved...while it is mostly there and I would still be happy with them but it is me pretending to be you. I understand I am not and there is probably a lot wrong that all of you would see instantly and this is why I am here.

Dropper Bottle: This is our final product mock up

Water Color: I am semi flexible here. This water color is slightly different on every level of our brand. The color itself can change...we are not stuck on THIS particular one. If you happen to make a new one that is similar in style and we use it...then I will happily commission you to change the rest on our next product run. I am pretty sure you can use this statement as evidence later . =) .

But seriously, we heavily believe in pay it forward and will work with anyone here that may have a vision bigger than ours. The winner of this contest will get preferential consideration on our marketing materials (need letterhead etc. next, as well as a brochure, and website) so three more projects coming down the pipeline.

Information to use for your mockup is contained on the card images I have included. I would prefer CBD for wellness CBD for life to be more prominent. No where else on the card do we have CBD mentioned.

Font styles to use
Sans Serif

Colors

Designer to choose colors to be used in the design.

Requirements
Must have
• Double Sided
• Front: OLU logo on front of card will be raised embossed. Background is watercolor. One has been provided. Others are up for consideration. If the rest of your design is incredible and I don't like your watercolor I will just ask to swap it.
• Back: Standard information. Not stuck on anything here. I LOVE clean minimal designs. The bleed on the card I provided is a luxury...
• Font for title and OLU is Adam. Everything else I prefer san serif or as clean as possible.
Nice to have
• I Need to incorporate Naturally Nurturing somewhere on the card. Bold but not intrusive.

```html
<!DOCTYPE html>
<html lang="en">
<head>
<meta charset="utf-8">
<title>OLU – Business Card</title>
<link rel="stylesheet" href="https://fonts.googleapis.com/css2?family=Source+Sans+3:wght@300;400;600&display=swap">
<style>
  :root {
    --paper: #ffffff;
    --ink: #1a1a1a;
    --icon-disc: #58585a;
    --wash-yellow: #fbe04a;
    --wash-gold: #f7b733;
    --wash-orange: #f59a4c;
    --wash-peach: #f6b79a;
    --wash-coral: #ef8a6a;
    --wash-cream: #fde9c8;
  }
  * { margin: 0; padding: 0; box-sizing: border-box; }
  html, body { width: 1200px; height: 738px; overflow: hidden; background: var(--paper); }
  body { position: relative; font-family: "Source Sans 3", sans-serif; color: var(--ink); }

  .card-side { position: absolute; top: 0; width: 523px; height: 738px; }
  .card-front { left: 0; }
  .card-back { left: 677px; }

  .watercolor-wash {
    position: absolute;
    background:
      radial-gradient(ellipse 45% 35% at 25% 20%, var(--wash-yellow) 0%, transparent 70%),
      radial-gradient(ellipse 40% 40% at 70% 25%, var(--wash-peach) 0%, transparent 70%),
      radial-gradient(ellipse 40% 35% at 40% 55%, var(--wash-gold) 0%, transparent 72%),
      radial-gradient(ellipse 35% 45% at 90% 60%, var(--wash-coral) 0%, transparent 70%),
      radial-gradient(ellipse 50% 40% at 15% 70%, var(--wash-orange) 0%, transparent 70%),
      linear-gradient(135deg, var(--wash-cream), var(--wash-peach));
  }
  .card-front .watercolor-wash {
    inset: 0 0 0 0;
    -webkit-mask-image: linear-gradient(to bottom, #000 0%, #000 62%, rgba(0,0,0,.35) 80%, transparent 96%);
    mask-image: linear-gradient(to bottom, #000 0%, #000 62%, rgba(0,0,0,.35) 80%, transparent 96%);
  }
  .card-back .watercolor-wash {
    left: 0; top: 0; width: 523px; height: 607px;
    -webkit-mask-image: linear-gradient(to bottom, transparent 0%, rgba(0,0,0,.25) 20%, #000 38%, #000 100%);
    mask-image: linear-gradient(to bottom, transparent 0%, rgba(0,0,0,.25) 20%, #000 38%, #000 100%);
  }

  .brand-lockup { position: absolute; left: 144px; top: 212px; width: 236px; text-align: center; }
  .brand-name { font-weight: 400; font-size: 104px; line-height: 1; letter-spacing: 6px; color: var(--ink); }
  .brand-tagline { margin-top: 6px; font-weight: 400; font-size: 21px; letter-spacing: 1.5px; text-transform: uppercase; color: var(--ink); white-space: nowrap; }

  .holder-name { position: absolute; left: 68px; top: 56px; font-size: 42px; font-weight: 400; line-height: 1.1; }
  .holder-title { position: absolute; left: 68px; top: 112px; font-size: 27px; font-weight: 400; letter-spacing: .5px; }

  .contact-icon { position: absolute; left: 94px; width: 44px; height: 44px; }
  .contact-text { position: absolute; left: 168px; font-size: 29px; line-height: 44px; font-weight: 400; }
  .icon-location { top: 270px; }
  .icon-phone { top: 389px; }
  .icon-web { top: 504px; }
  .text-address { top: 222px; }
  .text-phone { top: 385px; font-size: 38px; font-weight: 600; line-height: 52px; }
  .text-web { top: 483px; }

  .slogan { position: absolute; left: 0; top: 614px; width: 523px; text-align: center; font-weight: 300; font-size: 29px; line-height: 36px; }
  .slogan-dot { display: block; width: 8px; height: 8px; margin: 10px auto 10px; border-radius: 50%; background: var(--ink); }

  .edge-strip {
    position: absolute; left: 0; top: 727px; width: 523px; height: 11px;
    background: linear-gradient(90deg, var(--wash-gold), var(--wash-yellow) 55%, var(--wash-cream));
  }
</style>
</head>
<body>

<section class="card-side card-front">
  <div class="watercolor-wash" role="img" aria-label="Warm yellow, orange and peach watercolor wash fading to white at the bottom"></div>
  <div class="brand-lockup">
    <div class="brand-name">OLU</div>
    <div class="brand-tagline">Tonics of Vigor</div>
  </div>
</section>

<section class="card-side card-back">
  <div class="watercolor-wash" role="img" aria-label="Warm yellow, orange and coral watercolor wash fading to white at the top"></div>

  <h1 class="holder-name">Dana Whitfield</h1>
  <p class="holder-title">OWNER/CEO</p>

  <svg class="contact-icon icon-location" viewBox="0 0 44 44" aria-hidden="true">
    <circle cx="22" cy="22" r="22" fill="var(--icon-disc)"/>
    <path d="M22 11c-4.4 0-8 3.4-8 7.8 0 5.6 8 14.2 8 14.2s8-8.6 8-14.2c0-4.4-3.6-7.8-8-7.8z" fill="#fff"/>
    <circle cx="22" cy="19" r="3" fill="var(--icon-disc)"/>
  </svg>
  <p class="contact-text text-address">4120 W Canyon Ridge Dr<br>Peoria, AZ 85382<br>Suite 100</p>

  <svg class="contact-icon icon-phone" viewBox="0 0 44 44" aria-hidden="true">
    <circle cx="22" cy="22" r="22" fill="var(--icon-disc)"/>
    <path d="M15.5 12.5l4 4-2.3 2.6c1.4 2.9 3.8 5.3 6.7 6.7l2.6-2.3 4 4-2.2 3.2c-8.4-.6-15.2-7.4-15.8-15.8z" fill="#fff"/>
  </svg>
  <p class="contact-text text-phone">602 555 0148</p>

  <svg class="contact-icon icon-web" viewBox="0 0 44 44" aria-hidden="true">
    <circle cx="22" cy="22" r="22" fill="var(--icon-disc)"/>
    <g fill="none" stroke="#fff" stroke-width="2">
      <circle cx="22" cy="22" r="11"/>
      <ellipse cx="22" cy="22" rx="5" ry="11"/>
      <line x1="11" y1="22" x2="33" y2="22"/>
      <line x1="13" y1="16" x2="31" y2="16"/>
      <line x1="13" y1="28" x2="31" y2="28"/>
    </g>
  </svg>
  <p class="contact-text text-web">hello@olu.life<br>www.olu.life</p>

  <p class="slogan">CBD for wellness<span class="slogan-dot"></span>CBD for life</p>
  <div class="edge-strip"></div>
</section>

</body>
</html>
```